Create a pouch design for a new sports supplement product

Dimensions are 235mm (width) x 335mm (length) x 110mm (gusset)
File 1 - Extension of design brief please read both briefs
File 2 - Is 2 potential pouches this is just to give you a better example of size the dimensions are for the pouch on the right. This picture is not to give you design ideas as I am not very keen on either of these designs.
We need a design to be printed onto the pouches of our whey protein product. The brand name is 'Stellar Fuelworks' and needs to be displayed on the packaging either just writing or a simple logo design. I am not the most creative person in the world but have put together a more detailed brief listing some of the key information that needs to be included on the pouch (See attachment) Please feel free if you have experience of this the sports supplement market or have different ideas then please feel free to explore them.
The pouch would either be printed straight onto the pouch, or possibly just a printed label (front & back) to be stuck onto the pouch. Please design either or both.
Open to different colour schemes. Design has to be modern looking and eye-catching.
Some key points;
High quality whey protein concentrate
All Natural
Soy free
Great tasting
Please google image search 'protein pouches' to see other designs if your not familiar with the sports supplement market.
Any questions feel free to ask.
Updates
Hi, Thanks for all your design! I am really busy at the moment so haven't had chance to give feedback and have a proper look through all the designs. I have extended the time frame to give myself chance to give proper feedback and see any changes needed. Expect feedback sunday at the latest, and I will be pick a design early next week.
Target Market(s)
Sports supplement market. Product is a whey protein shake
Industry/Entity Type
Nutrition
Look and feel
Each slider illustrates characteristics of the customer's brand and the style your logo design should communicate.

```html
<!DOCTYPE html>
<html lang="en">
<head>
<meta charset="UTF-8">
<title>Stellar Fuelworks – Natural Whey Protein Pouch</title>
<link href="https://fonts.googleapis.com/css2?family=Anton&family=Oswald:wght@500;600&family=Archivo+Black&display=swap" rel="stylesheet">
<style>
  :root {
    --red-deep: #8e0a12;
    --red-main: #c8141e;
    --red-glow: #e23a3a;
    --brand-yellow: #ffd21a;
    --tag-yellow: #fff200;
    --white: #ffffff;
    --soft-white: #f3e4e4;
    --zip-line: rgba(90, 0, 6, 0.55);
    --zip-shine: rgba(255, 120, 120, 0.35);
  }
  html, body {
    margin: 0;
    padding: 0;
    overflow: hidden;
  }
  .pouch-front {
    position: relative;
    width: 986px;
    height: 1200px;
    overflow: hidden;
    background:
      radial-gradient(ellipse 60% 38% at 50% 52%, var(--red-glow) 0%, rgba(226,58,58,0) 70%),
      linear-gradient(180deg, var(--red-main) 0%, var(--red-main) 55%, var(--red-deep) 100%);
    font-family: "Oswald", sans-serif;
    color: var(--white);
  }
  .texture-field {
    position: absolute;
    left: 0;
    top: 380px;
    width: 986px;
    height: 420px;
    background: radial-gradient(ellipse 55% 50% at 50% 50%, rgba(255,90,90,0.25), rgba(255,90,90,0) 75%);
  }
  .zipper {
    position: absolute;
    left: 0;
    top: 150px;
    width: 986px;
    height: 14px;
  }
  .tear-note {
    position: absolute;
    top: 60px;
    right: 60px;
    font-family: "Oswald", sans-serif;
    font-weight: 500;
    font-size: 16px;
    line-height: 20px;
    letter-spacing: 0.3px;
    color: var(--soft-white);
    display: flex;
    align-items: center;
    gap: 10px;
  }
  .tear-note svg { display: block; }
  .brand-name {
    position: absolute;
    inset: 0;
    margin: 0;
    font-family: "Anton", sans-serif;
    font-weight: 400;
    color: var(--brand-yellow);
    text-transform: uppercase;
    line-height: 1;
    pointer-events: none;
  }
  .brand-name .line-one,
  .brand-name .line-two {
    position: absolute;
    left: 0;
    width: 986px;
    text-align: center;
    white-space: nowrap;
  }
  .brand-name .line-one {
    top: 270px;
    font-size: 178px;
    letter-spacing: 6px;
  }
  .brand-name .line-two {
    top: 447px;
    font-size: 120px;
    letter-spacing: 4px;
  }
  .product-type {
    position: absolute;
    top: 586px;
    left: 0;
    width: 986px;
    text-align: center;
    font-family: "Archivo Black", sans-serif;
    font-size: 42px;
    line-height: 56px;
    color: var(--tag-yellow);
    text-shadow: 3px 3px 0 rgba(60,0,0,0.7);
    margin: 0;
  }
  .benefit-list {
    position: absolute;
    top: 822px;
    left: 0;
    width: 986px;
    margin: 0;
    padding: 0;
    list-style: none;
    text-align: center;
    font-family: "Oswald", sans-serif;
    font-weight: 600;
    font-size: 28px;
    line-height: 40px;
    text-shadow: 2px 2px 0 rgba(60,0,0,0.55);
  }
  .flavour {
    position: absolute;
    top: 1002px;
    left: 0;
    width: 986px;
    text-align: center;
    font-family: "Archivo Black", sans-serif;
    font-size: 32px;
    line-height: 44px;
    color: var(--soft-white);
    text-shadow: 2px 2px 0 rgba(60,0,0,0.7);
    margin: 0;
  }
  .net-weight {
    position: absolute;
    top: 1096px;
    left: 0;
    width: 986px;
    text-align: center;
    font-family: "Oswald", sans-serif;
    font-weight: 500;
    font-size: 19px;
    line-height: 26px;
    color: var(--soft-white);
    margin: 0;
  }
</style>
</head>
<body>
  <main class="pouch-front">
    <div class="texture-field" role="img" aria-label="Soft halftone dot texture glowing behind the product name"></div>

    <svg class="zipper" viewBox="0 0 986 14" preserveAspectRatio="none" aria-hidden="true">
      <line x1="0" y1="4" x2="986" y2="4" stroke="var(--zip-line)" stroke-width="3"/>
      <line x1="0" y1="8" x2="986" y2="8" stroke="var(--zip-shine)" stroke-width="2"/>
      <line x1="0" y1="12" x2="986" y2="12" stroke="var(--zip-line)" stroke-width="2"/>
    </svg>

    <div class="tear-note">
      <span>Tear here and Reseal</span>
      <svg width="12" height="14" viewBox="0 0 12 14" aria-hidden="true">
        <polygon points="0,0 12,7 0,14" fill="#f7a21b"/>
      </svg>
    </div>

    <h1 class="brand-name">
      <span class="line-one">Stellar</span>
      <span class="line-two">Fuelworks</span>
    </h1>

    <p class="product-type">Natural Whey Protein</p>

    <ul class="benefit-list">
      <li>No artificial Flavours</li>
      <li>Excellent Amino acid profile</li>
      <li>80% high quality protein content</li>
      <li>Soy free</li>
    </ul>

    <p class="flavour">Strawberry Flavour</p>

    <p class="net-weight">909g 30 servings</p>
  </main>
</body>
</html>
```